Solmira Coast Island Weddings, Inc.

Solmira Coast Island Weddings Business Card design for Cardovelle. Clean, contemporary, creative, colorful (using colors provided). ONE SIDE SHOULD INCLUDE logo, www.solmiracoastweddings.com, @vowsbythecove. OTHER SIDE SHOULD INCLUDE Marisol Tennant. Owner & Officiant. Isabela, Puerto Rico. 555.407.1892. marisol@solmiracoastweddings.com. Colors are blue #58AA9E
and golden #e2bf80)

Target Market(s)

Destination Wedding Clients in the United States

Contact Information for Business Card

Marisol Tennant
Owner & Officiant
Isabela, Puerto Rico
555.407.1892
marisol@solmiracoastweddings.com

Font styles to use
Sans Serif

Requirements
Must have
• Colorful (colors are blue #58AA9E
• and golden #e2bf80), clean, contemporary. ONE SIDE SHOULD INCLUDE logo, www.solmiracoastweddings.com, @vowsbythecove. Other side should include Marisol Tennant. Owner & Officiant. Isabela, Puerto Rico. 555.407.1892. marisol@solmiracoastweddings.com
Nice to have
• I would like to see a version that includes my bio photo, and one that doesn't include the bio photo

```html
<!DOCTYPE html>
<html lang="en">
<head>
<meta charset="utf-8">
<title>Solmira Coast Island Weddings – Business Card</title>
<link href="https://fonts.googleapis.com/css2?family=Lato:wght@400;700&display=swap" rel="stylesheet">
<style>
  :root {
    --backdrop: #1d1d1f;
    --card: #141415;
    --card-edge: #1b1b1c;
    --gold: #e2bf80;
    --blue: #58aa9e;
    --text-soft: #b9b9b9;
    --blind: #2f2f30;
    --rule: #3a3a3b;
  }
  * { margin: 0; padding: 0; box-sizing: border-box; }
  html, body {
    width: 1200px;
    height: 900px;
    overflow: hidden;
    background: var(--backdrop);
    font-family: "Lato", Arial, sans-serif;
  }
  .canvas {
    position: relative;
    width: 1200px;
    height: 900px;
  }
  .card {
    position: absolute;
    width: 700px;
    height: 400px;
    background: linear-gradient(135deg, var(--card) 0%, var(--card-edge) 100%);
    border-radius: 3px;
  }
  .card--front { left: 300px; top: 35px; }
  .card--back  { left: 200px; top: 465px; }

  .brand-name {
    font-family: "Lato", Arial, sans-serif;
    font-weight: 400;
    text-align: center;
    letter-spacing: 0.06em;
    line-height: 1.25;
  }
  .brand-name .brand-line-small {
    display: block;
    font-size: 0.42em;
    letter-spacing: 0.3em;
    margin-top: 10px;
  }
  .card--front .brand-name {
    position: absolute;
    left: 0; right: 0; top: 140px;
    font-size: 40px;
    color: var(--gold);
  }
  .front-links {
    position: absolute;
    left: 0; right: 0; top: 300px;
    display: flex;
    justify-content: center;
    gap: 28px;
    font-size: 15px;
    letter-spacing: 0.04em;
    color: var(--blue);
  }

  .card--back .brand-name {
    position: absolute;
    left: 30px; top: 145px;
    width: 300px;
    font-size: 32px;
    color: var(--blind);
  }
  .divider {
    position: absolute;
    left: 355px; top: 85px;
    width: 1px; height: 230px;
    background: var(--rule);
  }
  .contact {
    position: absolute;
    left: 385px; top: 95px;
    color: var(--text-soft);
  }
  .contact-name {
    font-size: 26px;
    font-weight: 700;
    letter-spacing: 0.04em;
    text-transform: uppercase;
    color: var(--gold);
  }
  .contact-role {
    font-size: 16px;
    letter-spacing: 0.05em;
    color: var(--blue);
    margin-top: 2px;
  }
  .contact-dash {
    width: 10px; height: 1px;
    background: var(--blue);
    margin: 10px 0 14px;
  }
  .contact-list { list-style: none; }
  .contact-list li {
    display: flex;
    align-items: center;
    gap: 10px;
    font-size: 17px;
    line-height: 26px;
  }
  .contact-list svg { width: 12px; height: 12px; flex: none; }
</style>
</head>
<body>
<main class="canvas">
  <section class="card card--front">
    <p class="brand-name">Solmira Coast<span class="brand-line-small">ISLAND WEDDINGS</span></p>
    <div class="front-links">
      <span>www.solmiracoastweddings.com</span>
      <span>@vowsbythecove</span>
    </div>
  </section>

  <section class="card card--back">
    <p class="brand-name">Solmira Coast<span class="brand-line-small">ISLAND WEDDINGS</span></p>
    <div class="divider"></div>
    <div class="contact">
      <h1 class="contact-name">Marisol Tennant</h1>
      <p class="contact-role">Owner &amp; Officiant</p>
      <div class="contact-dash"></div>
      <ul class="contact-list">
        <li>
          <svg viewBox="0 0 12 12" aria-hidden="true"><path d="M6 11 Q2 6.5 2 4.5 A4 4 0 0 1 10 4.5 Q10 6.5 6 11 Z" fill="none" stroke="#58aa9e" stroke-width="1.2"/><circle cx="6" cy="4.5" r="1.4" fill="#58aa9e"/></svg>
          <span>Isabela, Puerto Rico</span>
        </li>
        <li>
          <svg viewBox="0 0 12 12" aria-hidden="true"><path d="M2.5 1 L4.5 1 L5 3.5 L3.8 4.3 Q4.8 6.8 7.7 8.2 L8.5 7 L11 7.5 L11 9.5 Q10.5 11 9 11 Q2 10 1 3 Q1 1.5 2.5 1 Z" fill="#58aa9e"/></svg>
          <span>555.407.1892</span>
        </li>
        <li>
          <svg viewBox="0 0 12 12" aria-hidden="true"><rect x="0.8" y="2.3" width="10.4" height="7.4" fill="none" stroke="#58aa9e" stroke-width="1.2"/><path d="M1 2.6 L6 6.6 L11 2.6" fill="none" stroke="#58aa9e" stroke-width="1.2"/></svg>
          <span>marisol@solmiracoastweddings.com</span>
        </li>
        <li>
          <svg viewBox="0 0 12 12" aria-hidden="true"><circle cx="6" cy="6" r="5" fill="none" stroke="#58aa9e" stroke-width="1.1"/><ellipse cx="6" cy="6" rx="2.2" ry="5" fill="none" stroke="#58aa9e" stroke-width="0.9"/><path d="M1 6 H11" stroke="#58aa9e" stroke-width="0.9"/></svg>
          <span>www.solmiracoastweddings.com</span>
        </li>
      </ul>
    </div>
  </section>
</main>
</body>
</html>
```